Sunridge Pilates Centre
Business Cards
Bright & Fun-filled
Maribel Foster
Owner/Certified Pilates Instructor
2847 Kestrel Dr Alder Vale AV 91873
n/A
do not have until sept 20
maribel@sunridgepilatescentre.com
www.sunridgepilatescentre.com
not sure but maybe? maybe logo or a Konrad Weller Quote or??

```html
<!DOCTYPE html>
<html lang="en">
<head>
<meta charset="utf-8">
<title>Sunridge Pilates Centre – Business Cards</title>
<link href="https://fonts.googleapis.com/css2?family=Montserrat:wght@400;500;600&display=swap" rel="stylesheet">
<style>
  :root {
    --backdrop: #dcd9d3;
    --card-black: #0c0c0c;
    --gold: #e2b21f;
    --gold-light: #f3cc3a;
    --gold-deep: #c8951a;
    --ink: #1a1a1a;
    --white: #f4f4f4;
  }
  * { margin: 0; padding: 0; box-sizing: border-box; }
  html, body {
    width: 1200px; height: 904px; overflow: hidden;
    background: var(--backdrop);
    font-family: "Montserrat", sans-serif;
  }
  .stage { position: relative; width: 1200px; height: 904px; }
  .card {
    position: absolute; left: 230px;
    width: 740px; height: 423px;
    background: var(--card-black);
    overflow: hidden;
    box-shadow: 0 10px 24px rgba(0,0,0,.28);
  }
  .card--back { top: 16px; }
  .card--front { top: 465px; }

  /* Back side */
  .brand-lockup {
    position: absolute; left: 0; right: 0; top: 150px;
    display: flex; flex-direction: column; align-items: center; gap: 14px;
  }
  .brand-mark {
    width: 46px; height: 46px; border-radius: 50%;
    border: 2px solid var(--gold);
  }
  .brand-name {
    color: var(--gold); font-weight: 500; font-size: 24px; letter-spacing: .5px;
  }
  .card--back .website {
    position: absolute; left: 0; right: 0; top: 292px; text-align: center;
  }
  .website {
    color: var(--gold); font-size: 13px; letter-spacing: 2.5px; font-weight: 400;
  }

  /* Front side */
  .front-brand {
    position: absolute; left: 34px; top: 42px;
    display: flex; flex-direction: column; align-items: center; gap: 8px; width: 150px;
  }
  .front-brand .brand-mark { width: 30px; height: 30px; border-width: 1.5px; }
  .front-brand .brand-name { font-size: 14px; text-align: center; line-height: 1.25; }
  .person {
    position: absolute; left: 368px; top: 80px;
  }
  .person-name { color: var(--gold); font-size: 22px; font-weight: 600; }
  .person-title { color: var(--white); font-size: 13px; margin-top: 6px; letter-spacing: .2px; }
  .corner-mark {
    position: absolute; right: 22px; top: 74px;
    width: 74px; height: 74px; border-radius: 50%;
    border: 2.5px solid var(--gold);
  }
  .contact-band {
    position: absolute; left: 0; top: 195px; width: 650px; height: 160px;
    background: linear-gradient(100deg, var(--gold-light), var(--gold) 55%, var(--gold-deep));
    clip-path: polygon(0 0, 100% 0, 92% 100%, 0 100%);
  }
  .contact-list {
    position: absolute; left: 40px; top: 236px; list-style: none;
    color: var(--ink); font-size: 13px; font-weight: 500;
  }
  .contact-list li { display: flex; align-items: flex-start; gap: 10px; margin-bottom: 8px; }
  .contact-list svg { width: 14px; height: 14px; flex: none; margin-top: 1px; }
  .address { line-height: 1.35; }
  .card--front .website { position: absolute; left: 40px; top: 382px; }
</style>
</head>
<body>
<main class="stage">

  <section class="card card--back" aria-label="Card back">
    <div class="brand-lockup">
      <span class="brand-mark"></span>
      <span class="brand-name">Sunridge Pilates Centre</span>
    </div>
    <p class="website">www.sunridgepilatescentre.com</p>
  </section>

  <section class="card card--front" aria-label="Card front">
    <div class="front-brand">
      <span class="brand-mark"></span>
      <span class="brand-name">Sunridge Pilates Centre</span>
    </div>

    <div class="person">
      <p class="person-name">Maribel Foster</p>
      <p class="person-title">Owner/Certified Pilates Instructor</p>
    </div>

    <span class="corner-mark"></span>

    <div class="contact-band"></div>
    <ul class="contact-list">
      <li>
        <svg viewBox="0 0 24 24" aria-hidden="true"><path d="M12 2a7 7 0 0 0-7 7c0 5 7 13 7 13s7-8 7-13a7 7 0 0 0-7-7zm0 9.5A2.5 2.5 0 1 1 12 6.5a2.5 2.5 0 0 1 0 5z" fill="#1a1a1a"/></svg>
        <span class="address">2847 Kestrel Dr<br>Alder Vale AV 91873</span>
      </li>
      <li>
        <svg viewBox="0 0 24 24" aria-hidden="true"><path d="M6.6 10.8a15.1 15.1 0 0 0 6.6 6.6l2.2-2.2a1 1 0 0 1 1-.25 11.4 11.4 0 0 0 3.6.57 1 1 0 0 1 1 1V20a1 1 0 0 1-1 1A17 17 0 0 1 3 4a1 1 0 0 1 1-1h3.5a1 1 0 0 1 1 1c0 1.25.2 2.45.57 3.57a1 1 0 0 1-.25 1z" fill="#1a1a1a"/></svg>
        <span>555-200-0147</span>
      </li>
      <li>
        <svg viewBox="0 0 24 24" aria-hidden="true"><rect x="3" y="5" width="18" height="14" rx="1.5" fill="none" stroke="#1a1a1a" stroke-width="2"/><path d="M3.5 6l8.5 7 8.5-7" fill="none" stroke="#1a1a1a" stroke-width="2"/></svg>
        <span>maribel@sunridgepilatescentre.com</span>
      </li>
    </ul>

    <p class="website">www.sunridgepilatescentre.com</p>
  </section>

</main>
</body>
</html>
```